Modern, Clean website for painting service.

We are working with a company called Brush Harbor and building a new website for them.

Some sites to use for content/competitors and inspiration:

https://www.coatwellcrew.example
https://ridgeline-coats.example
https://tevinhallorpainting.example

Thank you for taking the time to consider designing a website for us. We are web developers based in Stockton, CA, USA. Most of our projects go through the same process. Understanding this process may help you win a project with us. We custom-code all of our websites in-house. We don’t have any requirements as to what tools you use for your design, but we prefer Figma files. For any design that we label as four-stars, we send it to the client for review. The client picks the final design they want us to use. Once we complete this process, we will continue to show additional clients all the four-star sites and purchase them later. Your designs will have multiple chances to sell. For better chances of success, we ask that you follow these guidelines.

IMAGES:
If you use any images or icons in the design, we ask that you have a link to the asset so we can purchase the image/icon. Most of the designs we submit do not have the customer’s images on them unless they have some great images. Be creative; show us the feeling you are trying to portray with your image choices. Use any royalty-free site you choose. We subscribe to Adobe and mainly use their images, but we can purchase images outside of Adobe. PLEASE NOTE: we will not submit designs to clients with watermarks on the images.

FONTS:
We ask that you identify the fonts used in the design. This can be done in a message if you want. We typically use Google Fonts and Adobe Fonts.

CONTENT:
We're always open to different content and ideas. We often submit designs with stock images so the client can see our vision. We typically take pictures after the website launch to use their images with our vision. Lorem Ipsum is fine for paragraphs, but we ask that you write the headers in correct English. We want to be able to show the vision and identify the sections of the website.

INSPIRATION:
We typically add a couple of links in the brief of websites we like to help you get started in your design.

REVISIONS:
We do not often ask for revisions of the designs unless we see something in the design that may not appeal to the client. If there are slight changes that we want to make, we do that in the development process.

FEEDBACK:
We rarely give feedback on designs during the design process. We are working on many website projects and do not have the time to provide feedback. We usually respond if your request is well thought out and asks specific questions, but a note asking “feedback, please” usually goes unanswered.

```html
<!DOCTYPE html>
<html lang="en">
<head>
<meta charset="utf-8">
<title>Brush Harbor – Painting Services</title>
<link rel="stylesheet" href="https://fonts.googleapis.com/css2?family=Montserrat:wght@400;500;600;700;800&family=Open+Sans:wght@400;600;700&display=swap">
<style>
:root{
  --navy:#15264b;
  --navy-deep:#0f1c39;
  --red:#a51c2e;
  --red-dark:#8a1524;
  --ink:#1f2433;
  --muted:#5d6272;
  --light:#f2f2f4;
  --line:#dcdde3;
  --white:#ffffff;
  --sky:#4c7bb8;
}
*{box-sizing:border-box;margin:0;padding:0}
html,body{width:1200px;height:4464px;overflow:hidden}
body{font-family:"Open Sans",Arial,sans-serif;color:var(--ink);background:var(--white)}
h1,h2,h3,h4,.btn,.nav a,.label{font-family:"Montserrat",Arial,sans-serif}
.btn{display:inline-block;padding:13px 26px;font-size:12px;font-weight:700;letter-spacing:.8px;color:var(--white);text-transform:uppercase;text-decoration:none}
.btn-navy{background:var(--navy)}
.btn-red{background:var(--red)}
.section-title{font-size:34px;font-weight:600;text-align:center;text-transform:uppercase;letter-spacing:1px}
.title-red{color:var(--red)}
.title-white{color:var(--white)}
.title-rule{width:60px;height:3px;background:var(--red);margin:12px auto 0}

/* top bar & header */
.topbar{height:36px;background:var(--red);display:flex;justify-content:flex-end;align-items:center;padding:0 70px;gap:22px;color:var(--white);font-size:12px;font-weight:600}
.topbar .socials{display:flex;gap:8px}
.topbar .socials span{width:14px;height:14px;border-radius:50%;background:rgba(255,255,255,.85)}
.header{height:64px;display:flex;align-items:center;padding:0 70px;background:var(--white);box-shadow:0 2px 6px rgba(0,0,0,.06);position:relative;z-index:2}
.brand{display:flex;align-items:center;gap:10px;font-family:"Montserrat",sans-serif;font-weight:700;font-size:20px;color:var(--navy);letter-spacing:.5px}
.brand-mark{width:26px;height:26px;background:var(--red)}
.nav{display:flex;gap:28px;margin-left:auto;margin-right:28px}
.nav a{font-size:12px;font-weight:600;color:var(--navy);text-decoration:none;text-transform:uppercase}
.nav a.active{color:var(--red)}

/* hero */
.hero{height:470px;position:relative;background:linear-gradient(90deg,#dcd9d3 0%,#c9c5bd 22%,#2f5ea6 48%,#2d5ca3 72%,#e8e6e2 86%,#f1efec 100%)}
.hero-shade{position:absolute;inset:0;background:linear-gradient(90deg,rgba(15,28,57,.55) 0%,rgba(15,28,57,.2) 45%,rgba(0,0,0,0) 70%)}
.hero-copy{position:absolute;left:70px;top:130px;width:470px}
.hero-copy h1{font-size:52px;line-height:1.08;font-weight:800;color:var(--white);text-transform:uppercase}
.hero-copy .btn{margin-top:30px}

/* about */
.about{height:580px;display:flex;padding:110px 70px 0 175px;gap:60px}
.about-media{position:relative;width:400px;height:360px}
.about-house{position:absolute;left:0;top:0;width:330px;height:290px;background:linear-gradient(160deg,#6b7b8f,#2b3342 55%,#1a1f29)}
.about-badge{position:absolute;left:210px;top:36px;width:155px;height:74px;background:var(--red);color:var(--white);display:flex;align-items:center;gap:10px;padding:0 14px}
.about-badge strong{font-family:"Montserrat",sans-serif;font-size:40px;font-weight:800}
.about-badge span{font-size:12px;font-weight:700;text-transform:uppercase;line-height:1.25}
.about-worker{position:absolute;left:170px;top:170px;width:200px;height:200px;background:linear-gradient(135deg,#f3d23d,#e7b916 50%,#cfd4dc);border:5px solid var(--white)}
.about-copy{width:440px;padding-top:10px}
.about-copy h2{font-size:32px;font-weight:600;color:var(--red);text-transform:uppercase}
.about-copy .rule{width:60px;height:3px;background:var(--red);margin:10px 0 18px}
.about-copy h4{font-size:15px;font-weight:700;color:var(--ink);line-height:1.45;margin-bottom:14px}
.about-copy p{font-size:12.5px;line-height:1.75;color:var(--muted);margin-bottom:12px}
.about-copy .btn{margin-top:8px}

/* services */
.services{height:600px;position:relative;background:linear-gradient(180deg,var(--navy) 0%,var(--navy) 64%,var(--light) 64%,var(--light) 100%);overflow:hidden}
.services .section-title{padding-top:72px}
.service-track{position:absolute;top:170px;left:-112px;display:flex;gap:14px}
.service-card{width:232px;background:var(--white);box-shadow:0 6px 18px rgba(0,0,0,.12)}
.service-photo{height:250px}
.service-label{height:78px;display:flex;align-items:center;justify-content:space-between;padding:0 16px}
.service-label .label{font-size:15px;font-weight:700;color:var(--navy);text-transform:uppercase;line-height:1.2}
.service-arrow{width:30px;height:30px;border:1px solid var(--line);display:flex;align-items:center;justify-content:center}
.service-card.featured .label{color:var(--red)}
.service-card.featured .service-arrow{background:var(--red);border-color:var(--red)}
.dots{position:absolute;left:0;right:0;top:548px;display:flex;justify-content:center;align-items:center;gap:6px}
.dots span{width:8px;height:8px;border-radius:50%;background:#c5c8d0}
.dots .on{width:10px;height:10px;background:var(--red)}

/* gallery */
.gallery{height:480px;padding-top:78px;text-align:center}
.gallery-row{display:flex;justify-content:center;gap:14px;margin:44px 0 36px}
.gallery-row div{width:250px;height:180px}

/* why hire */
.why{height:490px;display:flex}
.why-panel{width:600px;background:var(--navy);padding:78px 70px 0 70px;color:var(--white)}
.why-panel h2{font-size:32px;font-weight:600;line-height:1.2;text-transform:uppercase}
.why-panel .rule{width:60px;height:3px;background:var(--red);margin:14px 0 34px}
.why-list{display:grid;grid-template-columns:1fr 1fr;gap:24px 30px;list-style:none}
.why-list li{display:flex;align-items:center;gap:14px;font-size:14px;line-height:1.35}
.why-icon{flex:none;width:38px;height:38px;border-radius:50%;border:2px solid rgba(255,255,255,.75);display:flex;align-items:center;justify-content:center}
.why-photo{flex:1;background:linear-gradient(120deg,#efe9e2 0%,#d9c3ad 40%,#c15b4a 62%,#8c6b57 80%,#e9e4dd 100%)}

/* testimonials */
.testimonials{height:340px;padding-top:56px;text-align:center}
.avatar{width:64px;height:64px;border-radius:50%;background:linear-gradient(135deg,#c9303f,#8a1524);margin:22px auto 16px}
.testimonials p{width:760px;margin:0 auto;font-size:12.5px;line-height:1.7;color:var(--muted)}
.testimonials .author{font-size:12px;color:var(--ink);font-weight:700;margin:10px 0 14px}

/* clients */
.clients{height:540px;background:var(--navy);padding-top:86px;text-align:center;position:relative}
.client-row{display:flex;justify-content:center;gap:26px;margin:48px 0 40px}
.client-box{width:200px;height:96px;background:var(--white);display:flex;align-items:center;justify-content:center;gap:10px;font-family:"Montserrat",sans-serif;font-weight:700;font-size:20px;color:var(--navy);letter-spacing:1px}
.client-box i{width:26px;height:26px;border-radius:50%;background:var(--red)}
.client-arrow{position:absolute;top:255px;width:30px;height:30px;display:flex;align-items:center;justify-content:center}

/* schedule */
.schedule{height:460px;padding-top:80px;text-align:center}
.steps{display:flex;justify-content:center;gap:8px;margin:40px 0 30px}
.step{width:190px;height:58px;display:flex;align-items:center;gap:12px;padding:0 16px;color:var(--white);font-family:"Montserrat",sans-serif;font-size:12px;font-weight:700;text-transform:uppercase;text-align:left;line-height:1.25}
.step b{font-size:18px}
.step-1{background:var(--red)}
.step-2{background:var(--sky)}
.step-3{background:#7d9dcb}
.fields{display:flex;justify-content:center;gap:14px;margin-bottom:30px}
.field{width:286px;height:44px;border:1px solid var(--line);display:flex;align-items:center;justify-content:space-between;padding:0 14px;font-size:13px;color:var(--muted)}

/* footer */
.footer{height:404px;background:var(--navy);color:var(--white);position:relative}
.footer-main{display:flex;padding:70px 70px 0 90px;gap:0}
.footer-brand{width:430px;display:flex;align-items:center;gap:14px;font-family:"Montserrat",sans-serif;font-weight:700;font-size:34px;letter-spacing:1px;padding-top:40px;align-self:flex-start}
.footer-brand i{width:52px;height:52px;background:var(--red)}
.footer-col{width:230px}
.footer-col h4{font-size:14px;font-weight:700;text-transform:uppercase;color:var(--white);margin-bottom:8px}
.footer-col .rule{width:36px;height:2px;background:var(--red);margin-bottom:18px}
.footer-col li{list-style:none;font-size:12.5px;line-height:2.1;color:#c8cfdd;display:flex;align-items:center;gap:8px}
.copyright{position:absolute;left:0;right:0;bottom:0;height:46px;background:var(--red);display:flex;align-items:center;justify-content:space-between;padding:0 70px;font-size:12px}
.copyright .socials{display:flex;gap:8px}
.copyright .socials span{width:18px;height:18px;border-radius:50%;background:rgba(255,255,255,.9)}
</style>
</head>
<body>

<div class="topbar">
  <span>NEED HELP? CALL US (209) 555-0147</span>
  <div class="socials"><span></span><span></span><span></span></div>
</div>

<header class="header">
  <div class="brand"><span class="brand-mark"></span>BRUSH HARBOR</div>
  <nav class="nav">
    <a class="active" href="#">Home</a><a href="#">About Us</a><a href="#">Services</a><a href="#">Gallery</a><a href="#">Testimonials</a><a href="#">Contact Us</a>
  </nav>
  <a class="btn btn-red" href="#">Book an Appointment</a>
</header>

<section class="hero" role="img" aria-label="Freshly painted room with a deep blue wall, a ladder and bright window light">
  <div class="hero-shade"></div>
  <div class="hero-copy">
    <h1>Best Quality of Paint for Home</h1>
    <a class="btn btn-navy" href="#">Discover More</a>
  </div>
</section>

<section class="about">
  <div class="about-media">
    <div class="about-house" role="img" aria-label="Modern two-storey house exterior at dusk"></div>
    <div class="about-badge"><strong>10</strong><span>Years of<br>Experience</span></div>
    <div class="about-worker" role="img" aria-label="Painter in a yellow hard hat holding a paint roller"></div>
  </div>
  <div class="about-copy">
    <h2>About Us</h2>
    <div class="rule"></div>
    <h4>Lorem Ipsum Is Simply Dummy Text Of The Printing And Typesetting Industry.</h4>
    <p>Lorem Ipsum has been the industry's standard dummy text ever since the 1500s, when an unknown printer took a galley of type and scrambled it to make a type specimen book.</p>
    <p>It has survived not only five centuries, but also the leap into electronic typesetting, remaining essentially unchanged. It was popularised in the 1960s with the release of Letraset sheets.</p>
    <a class="btn btn-navy" href="#">Discover More</a>
  </div>
</section>

<section class="services">
  <h2 class="section-title title-white">Our Services</h2>
  <div class="title-rule"></div>
  <div class="service-track">
    <div class="service-card">
      <div class="service-photo" role="img" aria-label="Red wooden fence being stained" style="background:linear-gradient(160deg,#b34a36,#7a2a20)"></div>
      <div class="service-label"><span class="label">Deck and<br>Fence Staining</span><span class="service-arrow"><svg width="12" height="12" viewBox="0 0 12 12"><path d="M4 2l4 4-4 4" fill="none" stroke="#15264b" stroke-width="1.8"/></svg></span></div>
    </div>
    <div class="service-card">
      <div class="service-photo" role="img" aria-label="Blue painted house exterior with white trim" style="background:linear-gradient(160deg,#3e6db3,#1f3f7a)"></div>
      <div class="service-label"><span class="label">Residential<br>Painting</span><span class="service-arrow"><svg width="12" height="12" viewBox="0 0 12 12"><path d="M4 2l4 4-4 4" fill="none" stroke="#15264b" stroke-width="1.8"/></svg></span></div>
    </div>
    <div class="service-card">
      <div class="service-photo" role="img" aria-label="Roller applying yellow coating to a wall" style="background:linear-gradient(160deg,#f2d54e,#d9a81b)"></div>
      <div class="service-label"><span class="label">Specialized<br>Coatings</span><span class="service-arrow"><svg width="12" height="12" viewBox="0 0 12 12"><path d="M4 2l4 4-4 4" fill="none" stroke="#15264b" stroke-width="1.8"/></svg></span></div>
    </div>
    <div class="service-card featured">
      <div class="service-photo" role="img" aria-label="Bright commercial office interior with fresh paint" style="background:linear-gradient(160deg,#e9e6e1,#b9b2a7)"></div>
      <div class="service-label"><span class="label">Commercial<br>Painting</span><span class="service-arrow"><svg width="12" height="12" viewBox="0 0 12 12"><path d="M4 2l4 4-4 4" fill="none" stroke="#fff" stroke-width="1.8"/></svg></span></div>
    </div>
    <div class="service-card">
      <div class="service-photo" role="img" aria-label="Living room with warm orange accent wall" style="background:linear-gradient(160deg,#e7a43f,#b8702a)"></div>
      <div class="service-label"><span class="label">Interior<br>Painting</span><span class="service-arrow"><svg width="12" height="12" viewBox="0 0 12 12"><path d="M4 2l4 4-4 4" fill="none" stroke="#15264b" stroke-width="1.8"/></svg></span></div>
    </div>
  </div>
  <div class="dots"><span></span><span></span><span class="on"></span><span></span><span></span></div>
</section>

<section class="gallery">
  <h2 class="section-title title-red">Gallery</h2>
  <div class="title-rule"></div>
  <div class="gallery-row">
    <div role="img" aria-label="Grey-blue suburban house with porch" style="background:linear-gradient(170deg,#a9bccf,#6f7f8c 60%,#5d7046)"></div>
    <div role="img" aria-label="Dark green painted home with gable roof" style="background:linear-gradient(170deg,#9fb2c4,#4d5c52 60%,#4f6a3a)"></div>
    <div role="img" aria-label="Light grey two-storey house with lawn" style="background:linear-gradient(170deg,#b8c8d8,#8b939c 60%,#5f7a44)"></div>
    <div role="img" aria-label="Cream and red brick family home" style="background:linear-gradient(170deg,#c3d2e0,#a68b78 60%,#5c7640)"></div>
  </div>
  <a class="btn btn-red" href="#">View All</a>
</section>

<section class="why">
  <div class="why-panel">
    <h2>Why Hire Brush Harbor<br>Painting?</h2>
    <div class="rule"></div>
    <ul class="why-list">
      <li><span class="why-icon"><svg width="16" height="16" viewBox="0 0 16 16"><path d="M3 8.5l3 3 7-7" fill="none" stroke="#fff" stroke-width="2"/></svg></span>Fully Licensed<br>&amp; Insured</li>
      <li><span class="why-icon"><svg width="16" height="16" viewBox="0 0 16 16"><circle cx="8" cy="8" r="6" fill="none" stroke="#fff" stroke-width="1.6"/><path d="M8 4.5V8l2.5 1.5" fill="none" stroke="#fff" stroke-width="1.6"/></svg></span>We Show Up<br>On Time</li>
      <li><span class="why-icon"><svg width="16" height="16" viewBox="0 0 16 16"><path d="M2 8l6-5 6 5v6H2z" fill="none" stroke="#fff" stroke-width="1.6"/></svg></span>Free In-Home<br>Estimate</li>
      <li><span class="why-icon"><svg width="16" height="16" viewBox="0 0 16 16"><path d="M3 8.5l3 3 7-7" fill="none" stroke="#fff" stroke-width="2"/></svg></span>We Do The<br>Job Right</li>
      <li><span class="why-icon"><svg width="16" height="16" viewBox="0 0 16 16"><path d="M8 13.5S2 10 2 6a3 3 0 016-1 3 3 0 016 1c0 4-6 7.5-6 7.5z" fill="none" stroke="#fff" stroke-width="1.6"/></svg></span>We Give Back To<br>Our Community</li>
      <li><span class="why-icon"><svg width="16" height="16" viewBox="0 0 16 16"><path d="M8 2v12M11 5H6.5a2 2 0 000 4h3a2 2 0 010 4H5" fill="none" stroke="#fff" stroke-width="1.6"/></svg></span>Up Front<br>Pricing</li>
      <li><span class="why-icon"><svg width="16" height="16" viewBox="0 0 16 16"><circle cx="5" cy="6" r="1.5" fill="#fff"/><circle cx="9" cy="4.5" r="1.5" fill="#fff"/><circle cx="12" cy="8" r="1.5" fill="#fff"/><path d="M8 14a6 6 0 110-12" fill="none" stroke="#fff" stroke-width="1.6"/></svg></span>Free Color<br>Consultation</li>
    </ul>
  </div>
  <div class="why-photo" role="img" aria-label="Couple choosing colors from a paint swatch fan"></div>
</section>

<section class="testimonials">
  <h2 class="section-title title-red">Testimonials</h2>
  <div class="avatar" role="img" aria-label="Customer portrait"></div>
  <p>Lorem Ipsum has been the industry's standard dummy text ever since the 1500s, when an unknown printer took a galley of type and scrambled it to make a type specimen book. It has survived not only five centuries, but also the leap into electronic typesetting, remaining essentially unchanged. It was popularised in the 1960s with the release of Letraset sheets.</p>
  <div class="author">— Dana Whitfield</div>
  <a class="btn btn-navy" href="#">View All</a>
</section>

<section class="clients">
  <h2 class="section-title title-white">Our Clients</h2>
  <div class="title-rule"></div>
  <span class="client-arrow" style="left:110px"><svg width="14" height="14" viewBox="0 0 14 14"><path d="M9 2L4 7l5 5" fill="none" stroke="#fff" stroke-width="2"/></svg></span>
  <div class="client-row">
    <div class="client-box"><i></i>LOREM</div>
    <div class="client-box"><i></i>LOREM</div>
    <div class="client-box"><i></i>LOREM</div>
    <div class="client-box"><i></i>LOREM</div>
  </div>
  <span class="client-arrow" style="right:110px"><svg width="14" height="14" viewBox="0 0 14 14"><path d="M5 2l5 5-5 5" fill="none" stroke="#fff" stroke-width="2"/></svg></span>
  <a class="btn btn-red" href="#">View All</a>
</section>

<section class="schedule">
  <h2 class="section-title title-red">Schedule an Estimate Now</h2>
  <div class="title-rule"></div>
  <div class="steps">
    <div class="step step-1"><b>01</b>Choose<br>Appointment</div>
    <div class="step step-2"><b>02</b>Your<br>Information</div>
    <div class="step step-3"><b>03</b>Confirmation</div>
  </div>
  <div class="fields">
    <div class="field">Select Date<svg width="12" height="8" viewBox="0 0 12 8"><path d="M1 1l5 5 5-5" fill="none" stroke="#5d6272" stroke-width="1.6"/></svg></div>
    <div class="field">Select Time<svg width="12" height="8" viewBox="0 0 12 8"><path d="M1 1l5 5 5-5" fill="none" stroke="#5d6272" stroke-width="1.6"/></svg></div>
  </div>
  <a class="btn btn-navy" href="#">Continue</a>
</section>

<footer class="footer">
  <div class="footer-main">
    <div class="footer-brand"><i></i>BRUSH HARBOR</div>
    <div class="footer-col">
      <h4>Contact Us</h4><div class="rule"></div>
      <ul>
        <li><svg width="12" height="12" viewBox="0 0 12 12"><path d="M2 1h2.5l1 3-1.5 1a6 6 0 003 3l1-1.5 3 1V10a1 1 0 01-1 1A9 9 0 011 2a1 1 0 011-1z" fill="#c8cfdd"/></svg>(209) 555-0147</li>
        <li><svg width="12" height="12" viewBox="0 0 12 12"><rect x="1" y="2.5" width="10" height="7" fill="none" stroke="#c8cfdd" stroke-width="1.2"/><path d="M1 3l5 3.5L11 3" fill="none" stroke="#c8cfdd" stroke-width="1.2"/></svg>hello@brushharbor.example</li>
        <li><svg width="12" height="12" viewBox="0 0 12 12"><path d="M6 11S2 7 2 4.5a4 4 0 018 0C10 7 6 11 6 11z" fill="#c8cfdd"/></svg>2415 Harbor Way, Stockton, CA</li>
      </ul>
    </div>
    <div class="footer-col">
      <h4>Services</h4><div class="rule"></div>
      <ul>
        <li>Residential Painting</li><li>Specialized Coatings</li><li>Commercial Painting</li><li>Interior Painting</li><li>Deck and Fence Staining</li>
      </ul>
    </div>
    <div class="footer-col">
      <h4>Quick Links</h4><div class="rule"></div>
      <ul>
        <li>About Us</li><li>Services</li><li>Gallery</li><li>Testimonials</li><li>Contact Us</li>
      </ul>
    </div>
  </div>
  <div class="copyright">
    <span>Copyright © 2024 Brush Harbor. All Rights Reserved.</span>
    <div class="socials"><span></span><span></span><span></span><span></span></div>
  </div>
</footer>

</body>
</html>
```